K&B RESTORATION

I want a brochure similiar to the example i've attached.
My company name is K&B Restoration. The website is: K-B-Restoration.com.
The phone number is 404.555.0173.

I don't like the "yellow" being the main color of the example so I'm open to suggestions. I want something CLEAN & Simple, like our logo . This will be a bi fold brochure

```html
<!DOCTYPE html>
<html lang="en">
<head>
<meta charset="utf-8">
<title>K&amp;B Restoration – Insurance Claim Specialist Brochure</title>
<link rel="stylesheet" href="https://fonts.googleapis.com/css2?family=Archivo+Black&family=Great+Vibes&family=Poppins:wght@400;600;700&display=swap">
<style>
  :root {
    --brand-blue: #3d56a9;
    --brand-blue-light: #5570bb;
    --paper: #f2f2f2;
    --ink: #1e1e1e;
    --backdrop: #e1e1e1;
    --link-blue: #2f4bb0;
  }
  * { box-sizing: border-box; margin: 0; padding: 0; }
  html, body { width: 1200px; height: 2359px; overflow: hidden; background: var(--backdrop); }
  body { font-family: "Poppins", sans-serif; color: var(--ink); position: relative; }

  .showcase-row { position: absolute; left: 0; width: 1200px; height: 786px; display: flex; align-items: center; justify-content: center; }
  .row-cover { top: 0; }
  .row-outer { top: 786px; }
  .row-inner { top: 1572px; }

  .page { position: relative; width: 440px; height: 600px; overflow: hidden; background: var(--paper); box-shadow: 0 10px 28px rgba(0,0,0,.16); }
  .spread { display: flex; box-shadow: 0 10px 28px rgba(0,0,0,.16); }
  .spread .page { box-shadow: none; }

  /* company name set as plain text */
  .brand-name { font-family: "Poppins", sans-serif; font-weight: 400; letter-spacing: 1px; font-size: 20px; color: var(--ink); white-space: nowrap; }
  .brand-name.on-blue { color: #fff; }

  /* front cover */
  .cover-top { position: absolute; top: 0; left: 0; right: 0; height: 130px; display: flex; align-items: center; justify-content: center; }
  .cover-body { position: absolute; top: 130px; left: 0; right: 0; bottom: 0; background: linear-gradient(160deg, var(--brand-blue) 40%, var(--brand-blue-light)); }
  .headline-frame { position: absolute; left: 40px; top: 95px; width: 360px; height: 220px; }
  .headline-frame svg { position: absolute; inset: 0; }
  .headline { position: absolute; left: 0; right: 0; top: 70px; text-align: center; color: #fff; }
  .headline-main { font-family: "Archivo Black", sans-serif; font-size: 34px; letter-spacing: -.5px; line-height: 1; }
  .headline-script { font-family: "Great Vibes", cursive; font-size: 38px; line-height: 1; margin-top: -4px; }
  .web-tab { position: absolute; left: 0; bottom: 0; width: 250px; height: 52px; background: var(--paper); clip-path: polygon(0 0, 100% 0, 88% 100%, 0 100%); display: flex; align-items: center; padding-left: 24px; font-size: 15px; color: var(--ink); }

  /* back cover */
  .blueprint-photo { position: absolute; top: 0; left: 0; right: 0; height: 380px; background: linear-gradient(150deg, #dfeaf6, #a9c4e2 55%, #cddcee); }
  .back-footer { position: absolute; left: 0; right: 0; bottom: 0; height: 220px; display: flex; align-items: center; justify-content: space-between; padding: 0 30px; }
  .back-footer .brand-name { font-size: 17px; }
  .contact-block h3 { font-size: 13px; font-weight: 700; color: var(--link-blue); letter-spacing: .5px; border-bottom: 1.5px solid var(--link-blue); padding-bottom: 4px; margin-bottom: 8px; }
  .contact-line { display: flex; align-items: center; gap: 6px; font-size: 12px; line-height: 1.7; }
  .contact-line svg { width: 11px; height: 11px; }

  /* inside spread */
  .kitchen-photo { position: absolute; inset: 0; background: linear-gradient(180deg, #d7dde0 0%, #c7ad8e 35%, #8a6d52 55%, #3c3a45 100%); }
  .inside-right .kitchen-photo { background: linear-gradient(180deg, #e3e8ea 0%, #d0cbc4 40%, #b9b2aa 100%); }
  .feature-panel { position: absolute; left: 60px; top: 170px; right: 0; bottom: 0; background: var(--brand-blue); padding: 34px 26px 0 32px; color: #fff; }
  .feature-panel .brand-name { display: block; text-align: center; margin-bottom: 28px; font-size: 19px; }
  .feature-list { list-style: none; }
  .feature-item { display: flex; gap: 14px; margin-bottom: 20px; }
  .feature-num { flex: none; width: 40px; height: 40px; border: 1.5px solid #fff; border-radius: 50%; display: flex; align-items: center; justify-content: center; font-size: 14px; }
  .feature-item h4 { font-size: 13px; font-weight: 700; letter-spacing: .3px; }
  .feature-item p { font-size: 10.5px; line-height: 1.35; }
  .feature-panel .web-tab { left: 0; width: 220px; font-size: 14px; color: var(--brand-blue); }
</style>
</head>
<body>

<section class="showcase-row row-cover">
  <article class="page front-cover">
    <header class="cover-top"><span class="brand-name">K&amp;B Restoration</span></header>
    <div class="cover-body">
      <div class="headline-frame">
        <svg viewBox="0 0 360 220" fill="none" stroke="#fff" stroke-width="4">
          <polyline points="90,2 2,2 2,110"/>
          <polyline points="270,218 358,218 358,110"/>
        </svg>
        <div class="headline">
          <div class="headline-main">Insurance Claim</div>
          <div class="headline-script">Specialist</div>
        </div>
      </div>
      <div class="web-tab">K-B-Restoration.com.</div>
    </div>
  </article>
</section>

<section class="showcase-row row-outer">
  <div class="spread">
    <article class="page back-cover">
      <div class="blueprint-photo" role="img" aria-label="Photo of rolled architectural blueprints"></div>
      <footer class="back-footer">
        <span class="brand-name">K&amp;B Restoration</span>
        <div class="contact-block">
          <h3>CONTACT US</h3>
          <div class="contact-line"><svg viewBox="0 0 12 12"><circle cx="6" cy="6" r="4.5" fill="none" stroke="currentColor" stroke-width="1.5"/></svg>K-B-Restoration.com.</div>
          <div class="contact-line"><svg viewBox="0 0 12 12"><path d="M2 1.5h2.5l1 2.5-1.5 1a6 6 0 0 0 3 3l1-1.5 2.5 1V11C5.5 11 1 6.5 2 1.5z" fill="currentColor"/></svg>404.555.0173.</div>
        </div>
      </footer>
    </article>
    <article class="page front-cover">
      <header class="cover-top"><span class="brand-name">K&amp;B Restoration</span></header>
      <div class="cover-body">
        <div class="headline-frame">
          <svg viewBox="0 0 360 220" fill="none" stroke="#fff" stroke-width="4">
            <polyline points="90,2 2,2 2,110"/>
            <polyline points="270,218 358,218 358,110"/>
          </svg>
          <div class="headline">
            <div class="headline-main">Insurance Claim</div>
            <div class="headline-script">Specialist</div>
          </div>
        </div>
        <div class="web-tab">K-B-Restoration.com.</div>
      </div>
    </article>
  </div>
</section>

<section class="showcase-row row-inner">
  <div class="spread">
    <article class="page inside-left">
      <div class="kitchen-photo" role="img" aria-label="Photo of a flooded modern kitchen"></div>
    </article>
    <article class="page inside-right">
      <div class="kitchen-photo" role="img" aria-label="Continuation of the flooded kitchen photo, ceiling and wall"></div>
      <div class="feature-panel">
        <span class="brand-name on-blue">K&amp;B Restoration</span>
        <ol class="feature-list">
          <li class="feature-item"><span class="feature-num">01</span><div><h4>LOREM IPSUM DOLOR</h4><p>Lorem ipsum dolor sit amet, consectetur adipiscing elit, sed do eiusmod tempor incididunt ut labore et</p></div></li>
          <li class="feature-item"><span class="feature-num">02</span><div><h4>LOREM IPSUM DOLOR</h4><p>Lorem ipsum dolor sit amet, consectetur adipiscing elit, sed do eiusmod tempor incididunt ut labore et</p></div></li>
          <li class="feature-item"><span class="feature-num">03</span><div><h4>LOREM IPSUM DOLOR</h4><p>Lorem ipsum dolor sit amet, consectetur adipiscing elit, sed do eiusmod tempor incididunt ut labore et</p></div></li>
        </ol>
        <div class="web-tab">K-B-Restoration.com.</div>
      </div>
    </article>
  </div>
</section>

</body>
</html>
```